Velmar Cyber Security (Consultants)

We need a webdesign for a new website www.velmarcybersecurity.example.

A draft version of the website is online. You can also look at our linkedIn company page: http://www.linkedin.example/company/7412096

This is what we do:
We defend our cybersociety against the growing number of cyber threats in order to allow our society to prosper and evolve more safely into the digital age. We seek to protect 4 key pillars of our society: critical (industrial) infrastructures, medical systems, our intellectual property, and financial systems.

Velmar is specialised in IT & information security consultancy and positions itself as an independent partner. Our employees possess a unique mix of technical hands-on engineering and consulting skills. We invest time and resources to learn about existing open-source and commercial technologies in order to give better advice.

We are no-nonsense, practical and to the point.

We advise and guide organisations with the strategy, definition and technical implementation of security projects. We take ownership in aligning the existing business, operational and technical context.

Some requirements:
- Ideally you deliver a fully coded and designed static website. I am hosting the website on www.hostbay.example; you can use the technologies that are supported there.
- My existing company colors and logos need to be preserved (see existing websites & linkedIn page)
- I would like a white background (is the best fit for my existing logo's, and easiest to maintain afterwards)
Some examples, but please feel free: http://www.stoneward.example/ http://www.quevix.example/ )
- I will use twitter as a way to update my website with relevant news ; So I want the twitterfeed integrated in the website, certianly on the homepage; if possible on all pages. (www.twitter.example/velmarsecurity)
- I am using my linkedIn company page; I want at least the "Follow" company button to be integrated in the website. (http://www.linkedin.example/company/velmar-cybersecurity-consultants/)
- it should be possible for me to do some minor updates to the site.
- I need several nice banners that I could also re-use at my linkedIn webpage (linkedIn requires 646 x 220 pixels or larger banners)

- As I see it now, the website should have a Home page that immediately displays the core services we offer. A basic Jobs page. an about and contact page where people can leave their details behind.
- Optional: An industries tab where there are sub-sites possible
Updates

This project has just been garantueed! First and second place get a nice payment. Please send you designs. 

I need
- A ready to deploy basic HTML webpage
- 4 pages: Home, Services, Careers, About/contact
- Some nice banners designed on my mission statement (in the brief)

Thanks

Reason: We would like to receive some more designs from other designers.

Target Market(s)

From medium sized KMO's, to mainly big enterprises.
My focusses is on strategic consulting, So managers, decision takers & business people
The site should also attrack consultants that have technical skills and managerial skills...

Industry/Entity Type

Financial

Requirements
Must have
• - My existing company colors and logos need to be preserved (see existing websites & linkedIn page)
- I would like a clean, professional site, with a white background
- As I see it now, the website should have a Home page that immediately displays the core services we offer. A basic careers page. an about and contact page where people can leave their details behind.
Nice to have
• - it should be possible for me to do some minor updates to the site.

```html
<!DOCTYPE html>
<html lang="en">
<head>
<meta charset="utf-8">
<title>Velmar Cyber Security</title>
<link href="https://fonts.googleapis.com/css2?family=Open+Sans:ital,wght@0,400;0,600;0,700;1,400&display=swap" rel="stylesheet">
<style>
:root{
  --red:#c4122f;
  --blue:#1a9ad6;
  --blue-dark:#0b5f93;
  --ink:#222;
  --grey-text:#555;
  --panel:#efeeee;
  --band:#f1f0f0;
  --footer:#464646;
  --green:#6fa33a;
  --white:#fff;
}
*{margin:0;padding:0;box-sizing:border-box}
html,body{width:1095px;height:1200px;overflow:hidden;background:var(--white)}
body{font-family:"Open Sans",Arial,sans-serif;color:var(--ink)}
.page{position:relative;width:1000px;height:1096px;transform:scale(1.095);transform-origin:0 0}
.abs{position:absolute}

.hero-band{left:0;top:58px;width:1000px;height:294px;background:var(--blue)}
.hero-photo{left:130px;top:58px;width:732px;height:294px;background:linear-gradient(100deg,#2a86c2 0%,#4aa6d8 45%,#9cc9e4 70%,#d8e6ef 100%)}
.header{left:171px;top:18px;width:658px;height:73px;background:var(--white);box-shadow:0 3px 6px rgba(0,0,0,.35)}
.logo{left:18px;top:14px}
.logo-name{font-size:32px;font-weight:600;color:var(--red);letter-spacing:-.5px;line-height:40px}
.follow{left:562px;top:-4px;text-align:right}
.follow small{display:block;font-size:7px;font-weight:700}
.follow b{font-size:16px;font-weight:700}
.nav{left:249px;top:37px;display:flex;height:36px}
.nav a{display:flex;align-items:center;justify-content:center;border-left:1px solid #ccc;font-size:12px;color:var(--ink);text-decoration:none}
.nav a.active{color:var(--red)}

.hero-title{left:171px;top:114px;font-size:20px;font-weight:700;color:var(--white)}
.hero-box{left:171px;top:152px;width:386px;height:137px;background:rgba(10,40,70,.45)}
.hero-list{list-style:none;left:190px;top:166px}
.hero-list li{display:flex;align-items:center;gap:18px;height:29.5px;font-size:13px;font-weight:600;color:var(--white)}
.btn{left:227px;top:307px;width:130px;height:28px;background:var(--green);color:var(--white);font-size:12px;font-weight:700;display:flex;align-items:center;justify-content:center;border-radius:2px}
.arrow{width:16px;height:28px;top:191px;background:var(--blue-dark);display:flex;align-items:center;justify-content:center}

.services{left:171px;top:384px;width:658px;height:299px;background:var(--panel);box-shadow:0 8px 8px -6px rgba(0,0,0,.35)}
.service{top:16px;width:146px}
.service h3{font-size:14.5px;font-weight:700;letter-spacing:.5px;line-height:18px;height:47px}
.service .pic{height:87px;border:2px solid #ccc}
.service p{margin-top:18px;font-size:10px;line-height:13px;height:94px;overflow:hidden;color:var(--ink)}
.more{display:flex;align-items:center;gap:6px;font-size:10.5px;color:var(--red)}

.clients-band{left:0;top:708px;width:1000px;height:192px;background:var(--band);border-top:1px solid #ddd}
.section-title{font-size:16.5px;font-weight:700;color:#444;letter-spacing:.3px}
.quote-mark{left:171px;top:758px;font-size:60px;font-weight:700;color:#c8c8c8;line-height:1}
.quote{left:222px;top:768px;width:385px;font-size:10px;line-height:14px;color:var(--grey-text)}
.quote p+p{margin-top:13px}
.tweet{left:663px;width:166px;background:var(--white);border:1px solid #ddd;padding:5px 9px;font-size:8.5px;line-height:11px;color:var(--grey-text)}
.tweet em{display:block;margin-bottom:4px}
.tweet span{color:var(--blue)}

.footer{left:0;top:900px;width:1000px;height:196px;background:var(--footer);color:var(--white)}
.fcol{top:22px}
.fcol h4{font-size:14.5px;font-weight:700;letter-spacing:.5px;display:inline-block;border-bottom:1px solid #999;padding-bottom:1px;margin-bottom:10px}
.fcol p{font-size:10px;line-height:12.5px}
.social-btn{display:block;width:70px;height:22px;background:var(--white);color:var(--ink);font-size:10.5px;font-weight:700;text-align:center;line-height:22px;margin-bottom:6px}
.footer-rule{left:171px;top:163px;width:658px;border-top:1px solid #777}
.copy{left:176px;top:173px;font-size:9px}
</style>
</head>
<body>
<div class="page">
  <div class="abs hero-band"></div>
  <div class="abs hero-photo" role="img" aria-label="Businessman in shirt and tie with arms crossed in front of a blurred server room"></div>

  <header class="abs header">
    <div class="abs logo"><span class="logo-name">Velmar</span></div>
    <div class="abs follow"><small>Follow us on</small><b>Linkora</b></div>
    <nav class="abs nav">
      <a class="active" style="width:68px">HOME</a>
      <a style="width:84px">SERVICES</a>
      <a style="width:83px">CAREERS</a>
      <a style="width:90px">ABOUT US</a>
      <a style="width:84px">CONTACT</a>
    </nav>
  </header>

  <h1 class="abs hero-title">WIN YOUR CYBER SECURITY BATTLES!</h1>
  <div class="abs hero-box"></div>
  <ul class="abs hero-list">
    <li><svg width="18" height="16"><path d="M1 8l5 6L17 1" fill="none" stroke="#9bd33c" stroke-width="2"/></svg>Learn what to do first!</li>
    <li><svg width="18" height="16"><path d="M1 8l5 6L17 1" fill="none" stroke="#9bd33c" stroke-width="2"/></svg>Stop spending into failing traditional security</li>
    <li><svg width="18" height="16"><path d="M1 8l5 6L17 1" fill="none" stroke="#9bd33c" stroke-width="2"/></svg>Shift to a real and automated security</li>
    <li><svg width="18" height="16"><path d="M1 8l5 6L17 1" fill="none" stroke="#9bd33c" stroke-width="2"/></svg>Win against global, professional and well</li>
  </ul>
  <div class="abs btn">LEARN MORE</div>
  <div class="abs arrow" style="left:155px"><svg width="8" height="12"><path d="M7 1L2 6l5 5" fill="none" stroke="#fff" stroke-width="1.5"/></svg></div>
  <div class="abs arrow" style="left:829px"><svg width="8" height="12"><path d="M1 1l5 5-5 5" fill="none" stroke="#fff" stroke-width="1.5"/></svg></div>

  <section class="abs services">
    <article class="abs service" style="left:16px">
      <h3>CRITICAL INFRASTRUCTURE</h3>
      <div class="pic" role="img" aria-label="Industrial control room panels" style="background:linear-gradient(#e8ecef,#9fa9b2)"></div>
      <p>Lorem Ipsum. Proin gravida nibh vel velit auctor aliquet. Aenean sollicitudin, lorem quis bibendum auctor,<br><br>Nnisi elit consequat ipsum, nec sagittis sem nibh id elit. Duis sed</p>
      <div class="more"><svg width="12" height="12"><circle cx="6" cy="6" r="6" fill="var(--red)"/><path d="M3 6h6M6 3l3 3-3 3" stroke="#fff" fill="none" stroke-width="1.4"/></svg>READ MORE</div>
    </article>
    <article class="abs service" style="left:177px">
      <h3>MEDICAL SYSTEMS</h3>
      <div class="pic" role="img" aria-label="Medical laboratory equipment" style="background:linear-gradient(#f4f6f8,#b9c3cb)"></div>
      <p>Lorem Ipsum. Proin gravida nibh vel velit auctor aliquet. Nnisi elit consequat<br>Iipsum, nec sagittis sem nibh id elit.<br><br>Duis sed odio sit amet nibh</p>
      <div class="more"><svg width="12" height="12"><circle cx="6" cy="6" r="6" fill="var(--red)"/><path d="M3 6h6M6 3l3 3-3 3" stroke="#fff" fill="none" stroke-width="1.4"/></svg>READ MORE</div>
    </article>
    <article class="abs service" style="left:336px">
      <h3>INTELLECTUAL PROPERTY</h3>
      <div class="pic" role="img" aria-label="Computer monitors showing data" style="background:linear-gradient(#2b4a66,#0f1c28)"></div>
      <p>Lorem Ipsum. Proin gravida nibh vel velit auctor aliquet.<br><br>Nnisi elit consequat<br>Iipsum, nec sagittis sem nibh id elit.</p>
      <div class="more"><svg width="12" height="12"><circle cx="6" cy="6" r="6" fill="var(--red)"/><path d="M3 6h6M6 3l3 3-3 3" stroke="#fff" fill="none" stroke-width="1.4"/></svg>READ MORE</div>
    </article>
    <article class="abs service" style="left:497px">
      <h3>FINANCIAL SYSTEMS</h3>
      <div class="pic" role="img" aria-label="Hands reviewing financial charts on a laptop" style="background:linear-gradient(120deg,#dfe5ea,#8fa3b5)"></div>
      <p>Lorem Ipsum. Proin gravida nibh vel velit auctor aliquet. Nnisi elit consequat<br><br>Iipsum, nec sagittis sem nibh id elit. Duis sed odio sit amet nibh vulputate.</p>
      <div class="more"><svg width="12" height="12"><circle cx="6" cy="6" r="6" fill="var(--red)"/><path d="M3 6h6M6 3l3 3-3 3" stroke="#fff" fill="none" stroke-width="1.4"/></svg>READ MORE</div>
    </article>
  </section>

  <div class="abs clients-band"></div>
  <h2 class="abs section-title" style="left:171px;top:734px">WHAT ARE SAYING OUR CLIENTS</h2>
  <div class="abs quote-mark">&ldquo;</div>
  <blockquote class="abs quote">
    <p>Lorem Ipsum. Proin gravida nibh vel velit auctor aliquet. Aenean sollicitudin, lorem quis bibendum auctor,</p>
    <p>Ipsum, nec sagittis sem nibh id elit. Duis sed odio sit amet nibh vulputate cursus a sit am nec tellus a odio tincidunt auctor a ornare odio.</p>
    <p style="text-align:right;margin-top:8px;color:var(--ink)">Dan Harlow - ASHFORD</p>
    <div class="more" style="justify-content:flex-end;margin-top:5px"><svg width="12" height="12"><circle cx="6" cy="6" r="6" fill="var(--red)"/><path d="M3 6h6M6 3l3 3-3 3" stroke="#fff" fill="none" stroke-width="1.4"/></svg>READ MORE TESTIMONIALS</div>
  </blockquote>

  <svg class="abs" style="left:628px;top:736px" width="20" height="18"><circle cx="10" cy="9" r="8" fill="var(--blue)"/></svg>
  <h2 class="abs section-title" style="left:663px;top:735px">LATEST TWEETS</h2>
  <div class="abs tweet" style="top:765px"><em>Posted 2 days ago</em><span>@marcusfen</span> Lorem ipsum dolor sit amet, consectetur adipiscing elit. Etiam sit amet justo nec dolor</div>
  <div class="abs tweet" style="top:827px"><em>Posted 5 days ago</em><span>@marcusfen</span> Lorem ipsum dolor sit amet, consectetur adipiscing elit.</div>

  <footer class="abs footer">
    <div class="abs fcol" style="left:171px"><h4>COMPANY</h4><p>About Us<br>History<br>Management<br>Leadership<br>Our Mission</p></div>
    <div class="abs fcol" style="left:359px"><h4>EXPERTISE</h4><p>Industrial Infrastructures<br>Medical Systems<br>Intellectual Property<br>Financial Systems<br>Cyber Threats</p></div>
    <div class="abs fcol" style="left:532px"><h4>CONNECT</h4><p>4120 Cedar Ave.<br>Ashford,<br><br>Phone: 987-555-0184<br>Fax: 987-555-0185<br>info@velmar.example</p></div>
    <div class="abs fcol" style="left:725px;top:20px"><h4 style="border:none">SOCIAL</h4>
      <span class="social-btn">Linkora</span><span class="social-btn">Vidstream</span><span class="social-btn">Friendbook</span>
    </div>
    <div class="abs footer-rule"></div>
    <p class="abs copy">Copyright © 2013 &nbsp;<b>VELMAR CYBER SECURITY</b>&nbsp; All rights reserved</p>
  </footer>
</div>
</body>
</html>
```